A book main title will be, "Kindle Your Clients"
The subtext will be, "Go to market with a story that sizzles"
Would like it to blend with my web site brand. You can find it here: www.kindleyourclients-demo.net

Audience is business and revenue leaders for small, medium and large businesses. They have a new solution, or want to enter a new market, and they need to "inspire their buyers" meaning getting the buyers to want to change enough to overcome their status quo bias. They need a story that sizzles to do this.

```html
<!DOCTYPE html>
<html lang="en">
<head>
<meta charset="utf-8">
<title>Kindle Your Clients — Book Cover</title>
<link rel="stylesheet" href="https://fonts.googleapis.com/css2?family=Montserrat:wght@400;600;800;900&display=swap">
<style>
  :root {
    --backdrop: #e6e6e6;
    --cover-teal: #2e9390;
    --cover-teal-dark: #27827f;
    --ink-light: #efefef;
    --ink-dark: #333333;
    --badge-fill: #ececec;
  }
  * { margin: 0; padding: 0; box-sizing: border-box; }
  html, body {
    width: 1200px;
    height: 800px;
    overflow: hidden;
    background: var(--backdrop);
  }
  .canvas {
    position: relative;
    width: 1200px;
    height: 800px;
    background: var(--backdrop);
  }
  .book-cover {
    position: absolute;
    left: 390px;
    top: 80px;
    width: 420px;
    height: 641px;
    background: var(--cover-teal);
    border-radius: 3px;
    font-family: "Montserrat", sans-serif;
    overflow: hidden;
  }
  .spine-hinge {
    position: absolute;
    left: 16px;
    top: 0;
    width: 3px;
    height: 100%;
    background: var(--cover-teal-dark);
  }
  .brand-badge {
    position: absolute;
    left: 75px;
    top: 16px;
    width: 268px;
    height: 268px;
    border-radius: 50%;
    background: var(--badge-fill);
    display: flex;
    align-items: center;
    justify-content: center;
  }
  .brand-name {
    color: var(--cover-teal);
    font-weight: 800;
    font-size: 22px;
    text-align: center;
    line-height: 1.2;
  }
  .title-block {
    position: absolute;
    left: 0;
    top: 303px;
    width: 100%;
    display: flex;
    flex-direction: column;
    align-items: center;
    text-transform: uppercase;
    font-weight: 900;
    line-height: 1;
  }
  .title-lead {
    color: var(--ink-light);
    font-size: 80px;
    letter-spacing: -2px;
  }
  .title-joiner {
    color: var(--ink-dark);
    font-size: 48px;
    letter-spacing: -1px;
    margin-top: 4px;
  }
  .title-main {
    position: relative;
    color: var(--ink-dark);
    font-size: 74px;
    letter-spacing: -2px;
    margin-top: 2px;
  }
  .trademark {
    position: absolute;
    right: -24px;
    top: 2px;
    font-size: 17px;
    font-weight: 800;
    letter-spacing: 0;
  }
  .subtitle {
    position: absolute;
    left: 0;
    top: 530px;
    width: 100%;
    text-align: center;
    color: var(--ink-dark);
    font-weight: 600;
    font-size: 17px;
  }
  .author {
    position: absolute;
    left: 0;
    top: 600px;
    width: 100%;
    text-align: center;
    color: var(--ink-light);
    font-weight: 400;
    font-size: 17px;
    letter-spacing: 0.5em;
    text-transform: uppercase;
  }
</style>
</head>
<body>
  <main class="canvas">
    <article class="book-cover">
      <div class="spine-hinge"></div>
      <div class="brand-badge">
        <span class="brand-name">Kindle Your<br>Clients</span>
      </div>
      <h1 class="title-block">
        <span class="title-lead">Kindle</span>
        <span class="title-joiner">Your</span>
        <span class="title-main">Clients<span class="trademark">TM</span></span>
      </h1>
      <p class="subtitle">Go to market with a story that sizzles</p>
      <p class="author">Dana Whitlock</p>
    </article>
  </main>
</body>
</html>
```